Swimming Pool Supply Company Business Cards

We need business cards designed for company. These need to be easy to edit so that we can fill in names, titles, and contact info for each person who works here.

Dalton R. Whitfield
Manager of Legal & Finance
K.L. Brisbane, Incorporated

4837 Grenway Avenue
Marlow Heights, PA 19243

E. dalton@klbrisbane-example.com
M. (215) 555-0173
O. (215) 555-0148

Contact Information for Business Card

Looking to upgrade current business cards with graphic that can be edited. Looking for fresh ideas for an age old industry.

Font styles to use
Serif
Sans Serif

Colors

Designer to choose colors to be used in the design.

Requirements
Must have
• Professional, fresh, unique but professional

```html
<!DOCTYPE html>
<html lang="en">
<head>
<meta charset="UTF-8">
<title>K.L. Brisbane Business Card</title>
<link href="https://fonts.googleapis.com/css2?family=Open+Sans:wght@400;700;800&display=swap" rel="stylesheet">
<style>
  :root {
    --blue-light: #3f8fcf;
    --blue-mid: #2f78b8;
    --blue-deep: #235896;
    --ink: #3a3a3c;
    --card-white: #f2f2f3;
    --page: #e4e6ea;
  }
  html, body {
    margin: 0;
    width: 1200px;
    height: 1023px;
    overflow: hidden;
    background: var(--page);
    font-family: "Open Sans", Arial, sans-serif;
  }
  .sheet {
    position: relative;
    width: 1200px;
    height: 1023px;
  }
  .card {
    position: absolute;
    left: 215px;
    width: 770px;
    height: 440px;
    border-radius: 28px;
    overflow: hidden;
    box-shadow: 0 6px 18px rgba(0,0,0,.18);
    background: var(--card-white);
  }
  .card--front { top: 48px; }
  .card--back { top: 535px; }
  .card__art {
    position: absolute;
    inset: 0;
    width: 100%;
    height: 100%;
  }
  .brand {
    position: absolute;
    left: 52px;
    top: 40px;
    color: var(--blue-mid);
  }
  .brand__name {
    font-size: 58px;
    font-weight: 800;
    letter-spacing: 1px;
    line-height: 1;
    margin: 0;
  }
  .brand__tagline {
    font-size: 17px;
    margin: 8px 0 0;
  }
  .person {
    position: absolute;
    left: 52px;
    top: 168px;
    color: var(--ink);
  }
  .person__name {
    font-size: 30px;
    font-weight: 700;
    margin: 0;
    line-height: 1.1;
  }
  .person__title {
    font-size: 18px;
    margin: 4px 0 14px;
  }
  .contact {
    list-style: none;
    margin: 0;
    padding: 0;
    font-size: 17px;
    line-height: 1.55;
  }
  .contact li {
    display: flex;
    align-items: center;
    gap: 10px;
  }
  .contact svg {
    width: 16px;
    height: 16px;
    flex: none;
  }
  .address {
    margin: 18px 0 0;
    font-size: 17px;
    line-height: 1.5;
  }
</style>
</head>
<body>
<main class="sheet">

  <section class="card card--front" aria-label="Business card front">
    <svg class="card__art" viewBox="0 0 770 440" preserveAspectRatio="none" aria-hidden="true">
      <path d="M520 0 H770 V440 H730 C800 280 720 90 520 0 Z" fill="#3f8fcf"/>
      <path d="M600 0 H770 V300 C760 170 700 70 600 0 Z" fill="#235896" opacity=".75"/>
      <path d="M560 0 C680 40 760 150 770 250 V440 H745 C790 260 700 80 560 0 Z" fill="#2f78b8" opacity=".6"/>
    </svg>

    <div class="brand">
      <p class="brand__name">BRISBANE</p>
      <p class="brand__tagline">Clear Water Starts Here, Service You Can Trust</p>
    </div>

    <div class="person">
      <h1 class="person__name">Dalton R. Whitfield</h1>
      <p class="person__title">Manager of Legal &amp; Finance</p>
      <ul class="contact">
        <li>
          <svg viewBox="0 0 16 16" aria-label="Mobile"><rect x="4" y="1" width="8" height="14" rx="1.5" fill="none" stroke="#2f78b8" stroke-width="1.6"/></svg>
          (215) 555-0173
        </li>
        <li>
          <svg viewBox="0 0 16 16" aria-label="Office"><path d="M4 2 L6.5 2 L7.5 5 L6 6.5 C7 8.5 8 9.5 9.5 10.5 L11 9 L14 10 L14 12.5 C14 13.5 13 14 12 14 C7 13.5 2.5 9 2 4 C2 3 3 2 4 2 Z" fill="#2f78b8"/></svg>
          (215) 555-0148
        </li>
        <li>
          <svg viewBox="0 0 16 16" aria-label="Email"><rect x="1" y="3" width="14" height="10" fill="none" stroke="#2f78b8" stroke-width="1.6"/><path d="M1 3 L8 9 L15 3 M1 13 L6 8 M15 13 L10 8" fill="none" stroke="#2f78b8" stroke-width="1.4"/></svg>
          dalton@klbrisbane-example.com
        </li>
      </ul>
      <p class="address">K.L. Brisbane, Incorporated<br>4837 Grenway Avenue, Marlow Heights, PA 19243</p>
    </div>
  </section>

  <section class="card card--back" aria-label="Business card back">
    <svg class="card__art" viewBox="0 0 770 440" preserveAspectRatio="none" aria-hidden="true">
      <defs>
        <linearGradient id="backBlue" x1="0" y1="0" x2="1" y2="1">
          <stop offset="0" stop-color="#3f8fcf"/>
          <stop offset="1" stop-color="#2a66a8"/>
        </linearGradient>
      </defs>
      <rect width="770" height="440" fill="url(#backBlue)"/>
      <path d="M0 60 C220 -10 520 20 770 150 V440 H0 Z" fill="#235896" opacity=".45"/>
      <ellipse cx="300" cy="250" rx="440" ry="170" fill="#f2f2f3"/>
      <path d="M0 330 C200 430 520 420 770 300 V440 H0 Z" fill="#2f78b8" opacity=".85"/>
      <path d="M0 380 C260 450 560 430 770 360 V440 H0 Z" fill="#235896" opacity=".6"/>
    </svg>
  </section>

</main>
</body>
</html>
```